Brick pressure cleaning business needs business cards that are memorable

The business is called Kestrel hydroblast brick and pressure cleaning.
we blast bricks on new houses and driveways. I would like a logo with water spraying out of the letter s in the wording. Also bricks on the card somehow and maybe the word kestrel to be on an angle above the rest of the business name if possible. some shinny gold would be nice somewhere to. Would like to list our services on the back of card- red and cream brick clean, green stain removal, floor scrapes, fence panel clean or changeout. Driveway cleans. hard surface pressure cleans.

Target Market(s)

Building companies and home reno people

Industry/Entity Type

construction

Contact Information for Business Card

business name,phone,number my name, services on the back

Colors
0054AA
0677BA
7BADD7
CADEEF
E8F1F8
FFF300
FFF600
FEFA6F
FFFEC7
FFFEE8

```html
<!DOCTYPE html>
<html lang="en">
<head>
<meta charset="utf-8">
<title>Kestrel Hydroblast – Business Cards</title>
<link href="https://fonts.googleapis.com/css2?family=Oswald:wght@600&family=Poppins:wght@400;500;600&display=swap" rel="stylesheet">
<style>
  :root {
    --backdrop: #2a2a2a;
    --card: #111111;
    --accent: #f39420;
    --brand-blue: #0677ba;
    --text-light: #f2f2f2;
    --divider: #8a8a8a;
  }
  * { box-sizing: border-box; margin: 0; padding: 0; }
  html, body {
    width: 1200px; height: 900px; overflow: hidden;
    background: var(--backdrop);
  }
  .sheet {
    position: relative; width: 1200px; height: 900px;
  }
  .card {
    position: absolute; left: 250px; width: 700px; height: 400px;
    background: var(--card);
    box-shadow: 0 12px 30px rgba(0,0,0,0.55);
    overflow: hidden;
  }
  .card::after {
    content: ""; position: absolute; left: 0; right: 0; bottom: 0;
    height: 12px; background: var(--accent);
  }
  .card--front { top: 40px; }
  .card--back { top: 460px; }

  /* front */
  .brand {
    position: absolute; left: 40px; top: 70px; width: 260px;
    display: flex; flex-direction: column; align-items: flex-start; gap: 14px;
  }
  .brand__mark {
    width: 70px; height: 70px; background: var(--brand-blue);
  }
  .brand__name {
    font-family: "Poppins", sans-serif; font-weight: 600;
    font-size: 22px; line-height: 1.25; color: var(--brand-blue);
    text-transform: uppercase; letter-spacing: 0.5px;
  }
  .services {
    position: absolute; left: 330px; top: 95px; list-style: none;
    font-family: "Poppins", sans-serif; font-weight: 500;
    font-size: 19px; line-height: 1.3; color: var(--text-light);
  }
  .services li { display: flex; align-items: center; gap: 14px; }
  .services li::before {
    content: ""; width: 16px; height: 6px; background: var(--accent); flex: none;
  }

  /* back */
  .person {
    position: absolute; left: 60px; top: 120px; width: 260px; text-align: right;
  }
  .person__name {
    font-family: "Oswald", sans-serif; font-weight: 600;
    font-size: 42px; line-height: 1.05; color: var(--accent);
    text-transform: uppercase;
  }
  .person__role {
    font-family: "Poppins", sans-serif; font-weight: 400;
    font-size: 20px; color: var(--text-light);
  }
  .card__divider {
    position: absolute; left: 345px; top: 112px; width: 1px; height: 90px;
    background: var(--divider);
  }
  .contact {
    position: absolute; left: 370px; top: 120px; list-style: none;
    font-family: "Poppins", sans-serif; font-weight: 500;
    font-size: 18px; line-height: 1.55; color: var(--text-light);
  }
  .contact li { display: flex; align-items: center; gap: 10px; }
  .contact svg { width: 18px; height: 18px; flex: none; }
  .address {
    position: absolute; left: 60px; right: 40px; top: 300px;
    font-family: "Poppins", sans-serif; font-weight: 400;
    font-size: 20px; color: var(--text-light);
  }
</style>
</head>
<body>
<main class="sheet">
  <section class="card card--front">
    <div class="brand">
      <div class="brand__mark"></div>
      <p class="brand__name">Kestrel hydroblast brick and pressure cleaning</p>
    </div>
    <ul class="services">
      <li>Red and cream brick clean</li>
      <li>Green stain removal</li>
      <li>Floor scrapes</li>
      <li>Fence panel clean or changeout</li>
      <li>Driveway cleans</li>
      <li>Hard surface pressure cleans</li>
    </ul>
  </section>

  <section class="card card--back">
    <div class="person">
      <h1 class="person__name">Daniel Reyes</h1>
      <p class="person__role">Managing Director</p>
    </div>
    <div class="card__divider"></div>
    <ul class="contact">
      <li>
        <svg viewBox="0 0 24 24" aria-hidden="true"><path fill="#f39420" d="M6.6 10.8a15.2 15.2 0 0 0 6.6 6.6l2.2-2.2a1 1 0 0 1 1-.25 11.4 11.4 0 0 0 3.6.57 1 1 0 0 1 1 1V20a1 1 0 0 1-1 1A17 17 0 0 1 3 4a1 1 0 0 1 1-1h3.5a1 1 0 0 1 1 1c0 1.25.2 2.45.57 3.57a1 1 0 0 1-.25 1z"/></svg>
        044-987 650 214
      </li>
      <li>
        <svg viewBox="0 0 24 24" aria-hidden="true"><rect x="2" y="5" width="20" height="14" fill="#f39420"/><path d="M2 5l10 8 10-8" fill="none" stroke="#111" stroke-width="1.8"/></svg>
        info@kestrelhydroblast.com
      </li>
      <li>
        <svg viewBox="0 0 24 24" aria-hidden="true"><g fill="none" stroke="#f39420" stroke-width="2"><circle cx="12" cy="12" r="9"/><ellipse cx="12" cy="12" rx="4" ry="9"/><path d="M3 12h18M5 7h14M5 17h14"/></g></svg>
        www.kestrelhydroblast.com
      </li>
    </ul>
    <p class="address">17 Harrow Lane, Brookvale, 45610</p>
  </section>
</main>
</body>
</html>
```